Marlo Tidy Yard Website

We need a website design for this new company. I've attached the company logo. This company is in the construction industry that provides general labor, maintenance and cleaning for construction sites. We want a clean and simple website that can be easy to navigate.

Target Market(s)

Construction industry

Industry/Entity Type

Construction

Number of Pages Required

2 page

Font styles to use
Sans Serif

```html
<!DOCTYPE html>
<html lang="en">
<head>
<meta charset="utf-8">
<title>Marlo Tidy Yard</title>
<link rel="stylesheet" href="https://fonts.googleapis.com/css2?family=Poppins:wght@300;400;500;600;700&display=swap">
<style>
:root{
  --navy:#0d0d6b;
  --orange:#ff6a00;
  --grey-btn:#9a9a9a;
  --topbar:#9e9e9e;
  --text:#3a3a3a;
  --body:#555;
  --footer:#1e1e1e;
  --white:#fff;
}
*{margin:0;padding:0;box-sizing:border-box}
html,body{width:1200px;height:2780px;overflow:hidden}
body{position:relative;font-family:"Poppins",sans-serif;color:var(--text);background:var(--white)}
.abs{position:absolute}
.topbar{left:0;top:0;width:1200px;height:26px;background:var(--topbar);color:var(--white);font-size:11px;display:flex;justify-content:flex-end;align-items:center;gap:14px;padding-right:96px;z-index:3}
.topbar svg{vertical-align:-2px;margin-right:5px}
.header{left:0;top:26px;width:1200px;height:54px;background:var(--white);z-index:3}
.nav{left:371px;top:0;height:54px;display:flex;align-items:center;gap:0;font-size:12px;font-weight:500;color:#555;letter-spacing:.3px}
.nav a{color:inherit;text-decoration:none;position:absolute;white-space:nowrap}
.nav a.active{color:var(--navy);font-weight:600}
.phone-box{left:903px;top:0;width:297px;height:54px;background:var(--orange);color:var(--white);font-size:20px;font-weight:600;display:flex;align-items:center;padding-left:34px;clip-path:polygon(14px 0,100% 0,100% 100%,0 100%)}
.phone-box svg{margin-right:8px}
.logo-disc{left:124px;top:0;width:168px;height:168px;border-radius:50%;background:var(--white);z-index:4;display:flex;align-items:center;justify-content:center;text-align:center;color:var(--navy);font-weight:700;font-size:21px;line-height:1.1}
.hero{left:0;top:0;width:1200px;height:618px;background:linear-gradient(120deg,#6f6d69 0%,#9b9892 35%,#b8b3aa 60%,#8c857b 100%)}
.hero-title{left:0;top:268px;width:1200px;text-align:center;color:var(--white);font-size:37px;font-weight:700}
.hero-sub{left:0;top:318px;width:1200px;text-align:center;color:var(--white);font-size:15px;line-height:24px}
.btn{display:flex;align-items:center;justify-content:center;color:var(--white);font-weight:600;text-decoration:none}
.btn-orange{background:var(--orange)}
.btn-grey{background:var(--grey-btn)}
.arrow{top:310px}
.svc-img{top:696px;width:262px;height:148px}
.svc-title{top:851px;font-size:17px;font-weight:600;color:var(--text)}
.svc-text{top:888px;width:270px;font-size:12px;line-height:24px;color:var(--body)}
.svc-btn{top:1004px;width:128px;height:29px;font-size:12px}
.trust-img{left:160px;top:1146px;width:448px;height:245px;background:linear-gradient(135deg,#8f8a80,#c7c1b4 50%,#6e6a63)}
.trust-title{left:653px;top:1150px;font-size:30px;font-weight:600;color:var(--navy)}
.trust-text{left:657px;top:1214px;width:410px;font-size:12.5px;line-height:23.5px;color:var(--text)}
.cta{left:0;top:1536px;width:1200px;height:347px;background:linear-gradient(100deg,#d9d6d0,#ecebe8 45%,#c9c4bb)}
.cta-title{left:0;top:1620px;width:1200px;text-align:center;font-size:32px;line-height:47px;font-weight:600;color:var(--text)}
.testi-title{left:0;top:1935px;width:1200px;text-align:center;font-size:41px;font-weight:700;color:var(--navy)}
.testi-sub{left:0;top:1997px;width:1200px;text-align:center;font-size:15px;color:var(--text)}
.quote{top:2058px;font-size:62px;font-weight:700;color:var(--orange);line-height:1;font-family:"Poppins",sans-serif}
.testi-text{top:2068px;width:230px;font-size:12.5px;line-height:26px;color:var(--body)}
.avatar{top:2174px;width:68px;height:68px;border-radius:50%;background:linear-gradient(#b9a58f,#6d5a4a)}
.testi-name{top:2196px;font-size:13px;color:var(--text)}
.footer{left:0;top:2328px;width:1200px;height:452px;background:var(--footer);color:var(--white)}
.foot-logo{left:163px;top:2470px;width:170px;font-size:26px;font-weight:700;line-height:1.15;color:var(--white)}
.foot-h{font-size:18px;font-weight:600}
.links{left:395px;top:2448px;list-style:none;font-size:13px}
.links li{height:35px;display:flex;align-items:center}
.links li::before{content:"";border-left:6px solid var(--white);border-top:4px solid transparent;border-bottom:4px solid transparent;margin-right:14px}
.links li.active{color:#2e8fe0}
.contact{left:577px;top:2448px;font-size:13px}
.contact .row{display:flex;align-items:center;gap:16px;margin-bottom:8px}
.contact .big{font-size:21px;font-weight:600}
.social{left:879px;top:2545px}
.social .circles{display:flex;gap:20px;margin-top:16px}
.social span{width:29px;height:29px;border-radius:50%;border:2px solid var(--orange);display:block}
.social span.fill{background:var(--orange)}
.rule{left:144px;top:2705px;width:912px;height:1px;background:#3c3c3c}
.copy{left:160px;top:2726px;font-size:11px}
.legal{right:140px;top:2726px;font-size:11px}
</style>
</head>
<body>

<div class="abs hero" role="img" aria-label="Photo of a worker vacuuming dust on a construction site floor"></div>

<div class="abs topbar">
  <span><svg width="12" height="9" viewBox="0 0 12 9"><rect x=".5" y=".5" width="11" height="8" fill="none" stroke="#fff"/><path d="M.5 .5 6 5l5.5-4.5" fill="none" stroke="#fff"/></svg>hello@marlotidyyard.com</span><span>|</span><span>LOGIN</span><span>|</span><span>REGISTER</span>
</div>

<header class="abs header">
  <nav class="abs nav">
    <a class="active" style="left:0">HOME</a>
    <a style="left:61px">SERVICES</a>
    <a style="left:145px">WHY CHOOSE US</a>
    <a style="left:269px">OUR PROCESS</a>
    <a style="left:378px">ABOUT</a>
    <a style="left:443px">CONTACT</a>
  </nav>
  <div class="abs phone-box"><svg width="14" height="16" viewBox="0 0 14 16"><path d="M3 1l3 3-2 2c1 2 3 4 5 5l2-2 3 3-2 3C7 15 0 8 1 3z" fill="#fff"/></svg>(000) 123-4567</div>
</header>
<div class="abs logo-disc"><span>Marlo<br>Tidy Yard</span></div>

<svg class="abs arrow" style="left:52px" width="20" height="40" viewBox="0 0 20 40"><path d="M18 2 2 20l16 18" fill="none" stroke="#fff" stroke-width="2"/></svg>
<svg class="abs arrow" style="left:1130px" width="20" height="40" viewBox="0 0 20 40"><path d="M2 2l16 18L2 38" fill="none" stroke="#fff" stroke-width="2"/></svg>

<h1 class="abs hero-title">Client-Centered Quality Service</h1>
<p class="abs hero-sub">Lorem ipsum dolor sit amet, consectetur adipiscing<br>elit. Vestibulum mattis tristique ipsum tristique quam.</p>
<a class="abs btn btn-orange" style="left:525px;top:380px;width:150px;height:34px;font-size:15px">&#9990; Get a Quote</a>

<section>
  <div class="abs svc-img" style="left:160px;background:linear-gradient(#a9c6e0,#d9dde2 60%,#6f7a6a)" role="img" aria-label="Photo of a modern office building"></div>
  <div class="abs svc-img" style="left:467px;background:linear-gradient(#b9c0c8,#8a8278 60%,#5e5a55)" role="img" aria-label="Photo of a worker pressure-washing a construction site"></div>
  <div class="abs svc-img" style="left:777px;background:linear-gradient(#9ec4e8,#c9b59a 55%,#6d8a4c)" role="img" aria-label="Photo of a suburban house with garden"></div>

  <h3 class="abs svc-title" style="left:160px">Commercial Cleaning</h3>
  <h3 class="abs svc-title" style="left:467px">Construction Cleaning</h3>
  <h3 class="abs svc-title" style="left:777px">Residential Cleaning</h3>

  <p class="abs svc-text" style="left:160px">Curabitur imperdiet in metus a tincidunt. In et augue ante. Vestibulum eget imperdiet odio. Nullam id lacus accumsan, blandit quam at, mollis ante.</p>
  <p class="abs svc-text" style="left:467px">Curabitur imperdiet in metus a tincidunt. In et augue ante. Vestibulum eget imperdiet odio. Nullam id lacus accumsan, blandit quam at, mollis ante.</p>
  <p class="abs svc-text" style="left:777px">Curabitur imperdiet in metus a tincidunt. In et augue ante. Vestibulum eget imperdiet odio. Nullam id lacus accumsan, blandit quam at, mollis ante.</p>

  <a class="abs btn btn-grey svc-btn" style="left:160px">Learn more</a>
  <a class="abs btn btn-orange svc-btn" style="left:467px">Learn more</a>
  <a class="abs btn btn-grey svc-btn" style="left:777px">Learn more</a>
</section>

<section>
  <div class="abs trust-img" role="img" aria-label="Photo of a worker scrubbing a concrete floor with a floor machine"></div>
  <h2 class="abs trust-title">Trusted, Quality Service</h2>
  <p class="abs trust-text">Curabitur lacinia mi sem, non scelerisque augue posuere sed. Integer mattis eget turpis id consequat. Phasellus et orci arcu. Sed vitae ultricies nisi. Mauris sed vulputate lorem. Mauris metus lectus, bibendum non erat at, efficitur venenatis tellus. Nullam non sagittis ex, sit amet convallis turpis. Curabitur nec euismod risus.</p>
  <a class="abs btn btn-grey" style="left:657px;top:1406px;width:128px;height:29px;font-size:12px">Read more</a>
</section>

<section>
  <div class="abs cta" role="img" aria-label="Faded photo of a worker vacuuming debris indoors"></div>
  <h2 class="abs cta-title">Have you been searching for<br>a cleaning solution?</h2>
  <a class="abs btn btn-orange" style="left:490px;top:1738px;width:219px;height:43px;font-size:17px">&#9990; Contact us today</a>
</section>

<section>
  <h2 class="abs testi-title">Testimonials</h2>
  <p class="abs testi-sub">See what people are saying about Marlo Tidy Yard</p>

  <div class="abs quote" style="left:169px">&ldquo;</div>
  <div class="abs quote" style="left:479px">&ldquo;</div>
  <div class="abs quote" style="left:785px">&ldquo;</div>

  <p class="abs testi-text" style="left:221px">Lorem ipsum dolor sit amet, consectetur adipiscing elit. Cura bitur bibendum dui at .</p>
  <p class="abs testi-text" style="left:531px">Lorem ipsum dolor sit amet, consectetur adipiscing elit. Cura bitur bibendum dui at .</p>
  <p class="abs testi-text" style="left:834px">Lorem ipsum dolor sit amet, consectetur adipiscing elit. Cura bitur bibendum dui at .</p>

  <div class="abs avatar" style="left:160px" role="img" aria-label="Customer portrait"></div>
  <div class="abs avatar" style="left:470px" role="img" aria-label="Customer portrait"></div>
  <div class="abs avatar" style="left:773px" role="img" aria-label="Customer portrait"></div>

  <span class="abs testi-name" style="left:241px">Owen R.</span>
  <span class="abs testi-name" style="left:551px">Nadia L.</span>
  <span class="abs testi-name" style="left:855px">Colin M.</span>
</section>

<footer class="abs footer"></footer>
<div class="abs foot-logo">Marlo<br>Tidy Yard</div>

<div class="abs" style="left:395px;top:2412px"><div class="foot-h" style="color:#fff">Quick Links</div></div>
<ul class="abs links" style="color:#fff">
  <li class="active">Home</li><li>Service</li><li>Why Choose Us</li><li>Our Prices</li><li>About Us</li><li>Contact</li>
</ul>

<div class="abs" style="left:577px;top:2412px"><div class="foot-h" style="color:#fff">Contact Info:</div></div>
<div class="abs contact" style="color:#fff">
  <div class="row" style="align-items:flex-start">
    <svg width="14" height="18" viewBox="0 0 14 18"><path d="M7 17S1 10 1 6.5a6 6 0 0 1 12 0C13 10 7 17 7 17z" fill="none" stroke="#fff"/><circle cx="7" cy="6.5" r="2" fill="none" stroke="#fff"/></svg>
    <span style="line-height:28px;margin-top:-5px">2210 Fenwick Ridge Road,<br>Dallas, TX 75201</span>
  </div>
  <div class="row">
    <svg width="18" height="18" viewBox="0 0 18 18"><path d="M4 1l3 4-2 2c1 3 3 5 6 6l2-2 4 3-2 3C8 17 1 10 1 4z" fill="none" stroke="#fff"/></svg>
    <span class="big">(000) 123-4567</span>
  </div>
  <div class="row">
    <svg width="20" height="18" viewBox="0 0 20 18"><rect x="5" y="1" width="10" height="5" fill="none" stroke="#fff"/><rect x="1" y="6" width="18" height="8" rx="1" fill="none" stroke="#fff"/><rect x="5" y="11" width="10" height="6" fill="none" stroke="#fff"/></svg>
    <span class="big">(000) 123-4567</span>
  </div>
  <div class="row">
    <svg width="18" height="12" viewBox="0 0 18 12"><rect x=".5" y=".5" width="17" height="11" fill="none" stroke="#fff"/><path d="M.5 .5 9 7l8.5-6.5" fill="none" stroke="#fff"/></svg>
    <span>hello@marlotidyyard.com</span>
  </div>
</div>

<div class="abs social">
  <div class="foot-h" style="color:#fff;font-size:17px">Follow us on</div>
  <div class="circles"><span></span><span class="fill"></span><span></span><span></span></div>
</div>

<div class="abs rule"></div>
<p class="abs copy" style="color:#fff">Marlo Tidy Yard. Copyright &copy; 2019. All rights reserved.</p>
<p class="abs legal" style="color:#fff">Legal Information &nbsp;|&nbsp; Privacy Policy &nbsp;|&nbsp; Contact Us</p>

</body>
</html>
```